Book cover: Stormy Days Survival for Kids (A5)

I have a book called Stormy Days Survival for Teens. It is a book for teenagers which gives them tips and tactics on how to survive life's challenges regarding friends, family, feelings, relationships and hard stuff in life generally. I will upload the cover of this book but you can see it on my past jobs as one of the designers her eon Pixel Bazaar did it for me.
I have a new book I've written called Stormy Days Survival for Kids. This is a parallel book to Stormy Days Survival for Teens, but it is specifically for 8 to 12 or 13 year olds, rather than for older teens.
A very important aspect of this job is that it SHOULD MATCH in some strong way - the Stormy Days Survival for Teens book. I will be selling them together, displaying them together and I want them to look like two of a pair. It might be that you use the same image as the first book but change the colour of the image so that it is bright orange and green perhaps? Or that there is another image but in the image is placed in the exact same position across the book as the first book. It needs to look like the books are by the same author.
However, I would like this one to look a bit "younger", more kid friendly. For example, a font that looks like it is for kids, or kids' writing perhaps.
I dont want to have photos on the book, and I dont think I want cartoons or drawings - because I'm not sure how this will tie in with the first book.
I want it to look modern, fresh and designed specifically for kids. The text needs to be:
Stormy Days Survival - For Kids!
Tips and ideas for 8 to 13 year olds about how to stay cool, calm and confident on even the toughest days!
The back cover is going to mostly just have the table of contents listed and a blurb, with one or two cartoons which I will supply. I am keen to pick a designer to just do the front cover first and will ask them to do the back cover later.
UPDATED: I have attached three files with fonts that I like.

```html
<!DOCTYPE html>
<html lang="en">
<head>
<meta charset="utf-8">
<title>Stormy Days Survival for Kids – Cover Spread</title>
<link rel="stylesheet" href="https://fonts.googleapis.com/css2?family=Anton&family=Oswald:wght@500;600&family=Righteous&family=Tinos&display=swap">
<style>
  :root {
    --page: #ffffff;
    --paper: #f6f5c6;
    --flourish: #fafadf;
    --fold: #ffffff;
    --band: #c89b66;
    --panel: #ffffff;
    --title: #e4532d;
    --ink: #1c1c1c;
    --ink-soft: #3b3b3d;
  }
  html, body {
    margin: 0;
    padding: 0;
    width: 1200px;
    height: 1000px;
    overflow: hidden;
    background: var(--page);
  }
  .cover-spread { display: block; width: 1200px; height: 1000px; }
  .paper { fill: var(--paper); }
  .fold-line { stroke: var(--fold); stroke-width: 1.5; }
  .band { fill: var(--band); }
  .title-panel { fill: var(--panel); }
  .title-main { font-family: "Anton", "Oswald", sans-serif; fill: var(--title); }
  .title-kids { font-family: "Righteous", "Arial Rounded MT Bold", sans-serif; fill: var(--title); }
  .subtitle { font-family: "Oswald", "Arial Narrow", sans-serif; font-weight: 600; fill: var(--ink); }
  .spine-title, .author-name { font-family: "Oswald", "Arial Narrow", sans-serif; font-weight: 600; fill: var(--ink-soft); }
  .author-role { font-family: "Tinos", "Times New Roman", serif; fill: var(--ink-soft); }
</style>
</head>
<body>
<svg class="cover-spread" viewBox="0 0 1200 1000" xmlns="http://www.w3.org/2000/svg">
  <defs>
    <radialGradient id="flourish-glow" cx="50%" cy="50%" r="55%">
      <stop offset="0%" stop-color="var(--flourish)"/>
      <stop offset="100%" stop-color="var(--paper)"/>
    </radialGradient>
  </defs>

  <!-- cover paper -->
  <rect class="paper" x="22" y="30" width="1156" height="940"/>

  <!-- flourish areas -->
  <g class="flourishes">
    <rect x="160" y="30" width="320" height="245" fill="url(#flourish-glow)" role="img" aria-label="Pale curling flourish ornament, back cover top"/>
    <rect x="160" y="720" width="320" height="250" fill="url(#flourish-glow)" role="img" aria-label="Pale curling flourish ornament, back cover bottom"/>
    <rect x="646" y="30" width="390" height="252" fill="url(#flourish-glow)" role="img" aria-label="Pale curling flourish ornament, front cover top"/>
    <rect x="646" y="716" width="390" height="254" fill="url(#flourish-glow)" role="img" aria-label="Pale curling flourish ornament, front cover bottom"/>
  </g>

  <!-- folds -->
  <line class="fold-line" x1="554" y1="30" x2="554" y2="970"/>
  <line class="fold-line" x1="646" y1="30" x2="646" y2="970"/>

  <!-- bands: spine -->
  <rect class="band" x="556" y="284" width="88" height="8"/>
  <rect class="band" x="556" y="298" width="88" height="8"/>
  <rect class="band" x="556" y="688" width="88" height="8"/>
  <rect class="band" x="556" y="705" width="88" height="8"/>
  <!-- bands: front -->
  <rect class="band" x="650" y="284" width="528" height="8"/>
  <rect class="band" x="650" y="298" width="528" height="8"/>
  <rect class="band" x="650" y="688" width="528" height="8"/>
  <rect class="band" x="650" y="705" width="528" height="8"/>

  <!-- front title panel -->
  <rect class="title-panel" x="648" y="311" width="530" height="374"/>

  <g class="front-title">
    <text class="title-main" x="688" y="450" font-size="104" textLength="447" lengthAdjust="spacingAndGlyphs">STORMY DAYS</text>
    <text class="title-main" x="688" y="552" font-size="104" textLength="447" lengthAdjust="spacingAndGlyphs">SURVIVAL</text>
    <text class="title-kids" x="1135" y="600" font-size="42" text-anchor="end" letter-spacing="4">for kids</text>
  </g>

  <text class="subtitle" x="656" y="637" font-size="13" textLength="514" lengthAdjust="spacingAndGlyphs">TIPS AND IDEAS FOR 8 TO 13 YEARS OLD ABOUT HOW TO STAY COOL, CALM and CONFIDENT EVEN ON THE TOUGHEST DAY</text>

  <!-- spine -->
  <text class="spine-title" transform="translate(588 312) rotate(90)" font-size="27" textLength="372" lengthAdjust="spacingAndGlyphs">STORMY DAYS SURVIVAL - FOR KIDS</text>
  <text class="author-name" transform="translate(590 732) rotate(90)" font-size="26" textLength="222" lengthAdjust="spacingAndGlyphs">MARLA QUENBY</text>
  <text class="author-role" transform="translate(570 770) rotate(90)" font-size="14">clinical psychologist</text>

  <!-- front author -->
  <text class="author-name" x="1044" y="918" font-size="28" text-anchor="middle" textLength="148" lengthAdjust="spacingAndGlyphs">MARLA QUENBY</text>
  <text class="author-role" x="1046" y="941" font-size="16" text-anchor="middle">clinical psychologist</text>
</svg>
</body>
</html>
```